Packaging Sales Box Design for small aquarium betta tank

We (Koru Fishworks) need a sales box design for our new finlet Q - small 1.3L aquarium for betta fish.
Go with 2 themes & 2 colour sales box - target for kids, boys & girls.

Product info & text, pictures and sales box die line are uploaded.

Final selected design will need to provide all source file to replace with final product pictures and in case and text change.

Best Regards,
Morris

Koru Fishworks

```html
<!DOCTYPE html>
<html lang="en">
<head>
<meta charset="utf-8">
<title>finlet Q – Children's Betta Starter Kit packaging</title>
<link rel="stylesheet" href="https://fonts.googleapis.com/css2?family=Open+Sans:ital,wght@0,600;0,700;0,800;1,600;1,700;1,800&display=swap">
<style>
  :root {
    --page-bg: #e9eaec;
    --water-top: #8fd3ec;
    --water-bottom: #4fb1d9;
    --side-top: #7cc6e4;
    --side-bottom: #3f9fcb;
    --banner-yellow: #f3ee3c;
    --banner-text: #1b2f8f;
    --accent-red: #e0201c;
    --bullet-text: #2a2e7a;
    --fine-text: #3d6f95;
    --pink-title: #d0237a;
    --pink-deep: #7a1d7e;
    --pink-gravel-a: #d83a86;
    --pink-gravel-b: #8a4fb3;
    --blue-title: #1e63a8;
    --blue-deep: #1d3f86;
    --blue-gravel-a: #2f6fc4;
    --blue-gravel-b: #48b86a;
    --bowl-glass: #dfeff3;
  }
  * { box-sizing: border-box; margin: 0; padding: 0; }
  html, body { width: 1200px; height: 1000px; overflow: hidden; }
  body {
    background: var(--page-bg);
    font-family: "Open Sans", Arial, sans-serif;
    display: flex;
    align-items: center;
    justify-content: center;
    gap: 30px;
  }
  .package { display: flex; box-shadow: 0 6px 20px rgba(0,0,0,.18); }
  .theme-pink { --title: var(--pink-title); --deep: var(--pink-deep); --gravel-a: var(--pink-gravel-a); --gravel-b: var(--pink-gravel-b); }
  .theme-blue { --title: var(--blue-title); --deep: var(--blue-deep); --gravel-a: var(--blue-gravel-a); --gravel-b: var(--blue-gravel-b); }

  /* side panels */
  .box-side {
    position: relative;
    width: 90px; height: 560px; overflow: hidden;
    background: linear-gradient(180deg, var(--side-top), var(--side-bottom));
  }
  .side-photo-child {
    position: absolute; left: 8px; top: 40px; right: 8px; bottom: 40px;
    border-radius: 6px;
    background: linear-gradient(180deg, #e8c9a8 0%, #7fa86a 45%, #d94a6a 100%);
  }
  .side-heading {
    position: absolute; left: 8px; right: 8px; top: 24px;
    font-size: 9px; font-weight: 800; font-style: italic; line-height: 1.25;
    color: var(--accent-red);
  }
  .side-copy {
    position: absolute; left: 8px; right: 8px; top: 66px;
    font-size: 7.5px; font-weight: 600; line-height: 1.35;
    color: var(--blue-deep);
  }
  .side-photo-fish {
    position: absolute; left: 10px; right: 10px; top: 290px; height: 150px;
    border-radius: 40px;
    background: linear-gradient(180deg, #f2f6f7, #9a4a5a 55%, #3c4e8e);
  }
  .side-caption {
    position: absolute; left: 8px; right: 8px; top: 452px;
    font-size: 7.5px; font-weight: 700; font-style: italic; line-height: 1.35;
    color: var(--blue-deep); text-align: center;
  }

  /* front panel */
  .box-front {
    position: relative;
    width: 480px; height: 560px; overflow: hidden;
    background: linear-gradient(180deg, var(--water-top), var(--water-bottom));
  }
  .product-name {
    position: absolute; left: 22px; top: 18px;
    font-size: 60px; font-weight: 800; line-height: 1;
    color: var(--title); letter-spacing: -1px;
  }
  .name-badge {
    position: absolute; left: 34px; top: 128px;
    width: 96px; height: 92px; border-radius: 22px;
    background: var(--deep);
  }
  .product-subtitle {
    position: absolute; left: 140px; top: 96px;
    font-size: 14px; font-weight: 800; font-style: italic;
    color: var(--deep);
  }
  .maker {
    position: absolute; right: 14px; top: 24px; width: 140px;
    text-align: center;
  }
  .maker-name {
    display: flex; align-items: center; justify-content: center; gap: 6px;
    font-size: 14px; font-weight: 800; color: var(--blue-deep); white-space: nowrap;
  }
  .maker-square { width: 13px; height: 13px; background: var(--accent-red); flex: none; }
  .maker-tagline {
    margin-top: 6px; font-size: 12px; font-weight: 700; font-style: italic;
    line-height: 1.3; color: var(--blue-deep);
  }
  .tank-photo {
    position: absolute; left: 160px; top: 175px;
    width: 290px; height: 300px; border-radius: 50%;
    background: radial-gradient(circle at 45% 40%, #ffffff 0%, var(--bowl-glass) 55%, #b8dbe6 100%);
  }
  .gravel-photo {
    position: absolute; left: 0; right: 0; bottom: 0; height: 80px;
    background: linear-gradient(90deg, var(--gravel-b), #ffffff 35%, var(--gravel-a) 65%, var(--gravel-b));
    opacity: .9;
  }
  .promo-banner {
    position: absolute; right: 8px; top: 140px; width: 265px; height: 104px;
  }
  .promo-banner svg { position: absolute; inset: 0; width: 100%; height: 100%; }
  .promo-text {
    position: absolute; inset: 14px 10px 16px 14px;
    font-size: 12.5px; font-weight: 800; font-style: italic; line-height: 1.35;
    color: var(--banner-text); text-align: center;
    transform: rotate(-4deg);
  }
  .promo-text em { color: var(--accent-red); }
  .led-pill {
    position: absolute; left: 34px; top: 234px;
    padding: 3px 10px; border-radius: 12px;
    background: var(--banner-yellow); border: 2px solid var(--deep);
    font-size: 11px; font-weight: 800; font-style: italic; color: var(--banner-text);
  }
  .feature-list {
    position: absolute; left: 28px; top: 322px;
    list-style: none;
    font-size: 15px; font-weight: 700; font-style: italic; line-height: 1.35;
    color: var(--bullet-text);
  }
  .feature-list li::before { content: "• "; }
  .spec-line {
    position: absolute; left: 28px; top: 426px;
    font-size: 10px; font-weight: 600; line-height: 1.5; color: var(--fine-text);
  }
</style>
</head>
<body>

  <div class="package theme-pink">
    <aside class="box-side side-photo" aria-label="Box side panel, pink theme">
      <div class="side-photo-child" role="img" aria-label="Photo of a child with a betta tank"></div>
    </aside>
    <section class="box-front" aria-label="finlet Q box front, pink theme">
      <div class="tank-photo" role="img" aria-label="Product photo: round 1.3L tank with a betta fish and pink gravel"></div>
      <div class="gravel-photo" role="img" aria-label="Photo band of pink, purple and white aquarium gravel"></div>
      <h1 class="product-name">finlet Q</h1>
      <span class="name-badge"></span>
      <p class="product-subtitle">Children's Betta Starter Kit</p>
      <div class="maker">
        <div class="maker-name"><span class="maker-square"></span>Koru Fishworks</div>
        <p class="maker-tagline">Adds life to your environment</p>
      </div>
      <div class="promo-banner">
        <svg viewBox="0 0 300 120" preserveAspectRatio="none"><path d="M6 22 Q150 -4 294 8 L292 96 Q150 86 10 118 Z" fill="var(--banner-yellow)" stroke="#1d3f86" stroke-width="2"/></svg>
        <p class="promo-text">The ideal <em>FIRST PET</em> for your child<br>Teach your child great life lessons<br>with their first pet fish</p>
      </div>
      <span class="led-pill">with LED Light!</span>
      <ul class="feature-list">
        <li>Teaches Responsibility</li>
        <li>EZ Care</li>
        <li>A Great Living Night-Light !</li>
      </ul>
      <p class="spec-line">Model #KF01L-OPK<br>Tank capacity: 1.3L (TBC)</p>
    </section>
  </div>

  <div class="package theme-blue">
    <section class="box-front" aria-label="finlet Q box front, blue theme">
      <div class="tank-photo" role="img" aria-label="Product photo: round 1.3L tank with a betta fish and blue-green gravel"></div>
      <div class="gravel-photo" role="img" aria-label="Photo band of blue, green and white aquarium gravel"></div>
      <h1 class="product-name">finlet Q</h1>
      <span class="name-badge"></span>
      <p class="product-subtitle">Children's Betta Starter Kit</p>
      <div class="maker">
        <div class="maker-name"><span class="maker-square"></span>Koru Fishworks</div>
        <p class="maker-tagline">Adds life to your environment</p>
      </div>
      <div class="promo-banner">
        <svg viewBox="0 0 300 120" preserveAspectRatio="none"><path d="M6 22 Q150 -4 294 8 L292 96 Q150 86 10 118 Z" fill="var(--banner-yellow)" stroke="#1d3f86" stroke-width="2"/></svg>
        <p class="promo-text">The ideal <em>FIRST PET</em> for your child<br>Teach your child great life lessons<br>with their first pet fish</p>
      </div>
      <span class="led-pill">with LED Light!</span>
      <ul class="feature-list">
        <li>Teaches Responsibility</li>
        <li>EZ Care</li>
        <li>A Great Living Night-Light !</li>
      </ul>
      <p class="spec-line">Model #KF01L-OPK<br>Tank capacity: 1.3L (TBC)</p>
    </section>
    <aside class="box-side side-info" aria-label="Box side panel, blue theme">
      <h2 class="side-heading">Why a betta makes a great first pet</h2>
      <p class="side-copy">Bettas are hardy, colourful fish that need little space. Feed a few pellets daily, change a third of the water each week and keep the tank away from direct sun. Your child will love watching their fish grow.</p>
      <div class="side-photo-fish" role="img" aria-label="Photo of a red and blue betta fish"></div>
      <p class="side-caption">Tank shown with optional gravel.</p>
    </aside>
  </div>

</body>
</html>
```